Hip-Hop Artist RT Marble new album cover design for "Quiet Engines"

Artist: RT Marble
Album Title: Quiet Engines
I am attaching a un-edited picture to use & some sample images with the "Quiet Engines" concept directions. I am hoping that the graphic designers accepting this challenge can do a better or different job than the 3 sample design images attached. I do like each of the 3 attached drafts(Draft, Draft2, Draft3) concepts. But, would like to see other creative design approaches and other possible affect. artwork ideas.
I am also attaching a number of random design that I also like the direction on.
Please let em know if you have any questions, and I will respond as quickly as possible.

```html
<!DOCTYPE html>
<html lang="en">
<head>
<meta charset="utf-8">
<title>RT Marble — Quiet Engines</title>
<link rel="stylesheet" href="https://fonts.googleapis.com/css2?family=Cinzel:wght@500&family=Quicksand:wght@400&display=swap">
<style>
  :root {
    --bg-deep: #120606;
    --photo-warm: #5a3a34;
    --photo-skin: #b98a78;
    --photo-shadow: #1c1414;
    --tint-red: #4a0709;
    --tint-red-deep: #2a0203;
    --tint-grey: #2b2828;
    --title-white: #ffffff;
    --title-grey: #c6bfbf;
    --title-echo: #3a3434;
    --artist-shadow: #6a0a0d;
  }
  html, body {
    margin: 0;
    padding: 0;
    width: 1200px;
    height: 1108px;
    overflow: hidden;
    background: var(--bg-deep);
  }
  .cover {
    position: relative;
    width: 1200px;
    height: 1108px;
    overflow: hidden;
  }
  .cover__art {
    position: absolute;
    inset: 0;
    display: block;
  }
  .title {
    font-family: "Quicksand", sans-serif;
    font-weight: 400;
    font-size: 236px;
  }
  .artist-name {
    font-family: "Cinzel", serif;
    font-weight: 500;
    font-size: 50px;
    letter-spacing: 1px;
  }
</style>
</head>
<body>
<main class="cover">
  <svg class="cover__art" width="1200" height="1108" viewBox="0 0 1200 1108">
    <defs>
      <radialGradient id="portrait-tones" cx="0.5" cy="0.4" r="0.7">
        <stop offset="0" stop-color="var(--photo-skin)"/>
        <stop offset="0.35" stop-color="var(--photo-warm)"/>
        <stop offset="1" stop-color="var(--photo-shadow)"/>
      </radialGradient>
      <linearGradient id="title-fill" gradientUnits="userSpaceOnUse" x1="0" y1="0" x2="1200" y2="0">
        <stop offset="0" stop-color="var(--title-white)"/>
        <stop offset="0.5" stop-color="var(--title-white)"/>
        <stop offset="0.5" stop-color="var(--title-grey)"/>
        <stop offset="1" stop-color="var(--title-grey)"/>
      </linearGradient>
    </defs>

    <rect class="portrait" x="0" y="0" width="1200" height="1108" fill="url(#portrait-tones)"
          role="img" aria-label="Portrait photo of the artist leaning toward the camera in a dark shirt and patterned tie"/>

    <g class="colour-blocks">
      <rect x="0" y="0" width="400" height="552" fill="var(--tint-red)" opacity="0.78"/>
      <rect x="400" y="0" width="400" height="552" fill="var(--tint-red-deep)" opacity="0.15"/>
      <rect x="800" y="0" width="400" height="552" fill="var(--tint-grey)" opacity="0.85"/>
      <rect x="0" y="552" width="400" height="556" fill="var(--tint-grey)" opacity="0.55"/>
      <rect x="400" y="552" width="400" height="556" fill="var(--tint-red-deep)" opacity="0.88"/>
      <rect x="800" y="552" width="400" height="556" fill="var(--tint-red)" opacity="0.8"/>
    </g>

    <g class="title-echo" fill="var(--title-echo)" opacity="0.55">
      <text class="title" x="190" y="558" textLength="830" lengthAdjust="spacingAndGlyphs">QUIET</text>
      <text class="title" x="24" y="762" textLength="1116" lengthAdjust="spacingAndGlyphs">ENGINES</text>
    </g>

    <g class="title-main" fill="url(#title-fill)">
      <text class="title" x="212" y="540" textLength="828" lengthAdjust="spacingAndGlyphs">QUIET</text>
      <text class="title" x="40" y="744" textLength="1116" lengthAdjust="spacingAndGlyphs">ENGINES</text>
    </g>

    <g class="artist">
      <text class="artist-name" x="608" y="1072" text-anchor="middle" fill="var(--artist-shadow)">RT MARBLE</text>
      <text class="artist-name" x="605" y="1069" text-anchor="middle" fill="var(--title-white)">RT MARBLE</text>
    </g>
  </svg>
</main>
</body>
</html>
```